New Meal Prep Flyer for New Package Deals

We are looking for a design that displays our new packages that we offer. If you take a look at our website www.brambleforkmeals.com, and click on packages , you'll see the way we display them currently . We would like something similar to that in style . The first package is called "Horizon" and this package will be a 1 week package (7 days ), 2 meals a day, for a price of $195.00. The second package is called "Amber" and this package will be a 3 week package (21 days) 2 meals per day, for a price of $546.00 , the third package is a 6 week+ package (45 days), and it is called "Evergreen" , 2 meals per day , and the price is $1080.00 .
For the Amber Package , can you put next to it "Save $42.00!"
For the Evergreen Package, can you put next to it "Save $180!"
We also want our logo on the flyer (see attached), and we are just looking for a 1 page flyer , 8 1/2 x 11.

```html
<!DOCTYPE html>
<html lang="en">
<head>
<meta charset="utf-8">
<title>Bramblefork Meal Prep Packages</title>
<link rel="stylesheet" href="https://fonts.googleapis.com/css2?family=Montserrat:wght@600;700;800&family=Oswald:wght@700&display=swap">
<style>
  :root {
    --green: #8dc21f;
    --green-dark: #74a316;
    --orange: #ec7c0e;
    --orange-dark: #c9650a;
    --grey: #9b9b9b;
    --grey-dark: #7f7f7f;
    --ink: #2e2e2e;
    --red: #d9141b;
    --paper: #f3f3f3;
    --stage: #efefef;
    --line: #cfcfcf;
  }
  * { box-sizing: border-box; margin: 0; padding: 0; }
  html, body { width: 783px; height: 1200px; overflow: hidden; }
  body {
    background: var(--stage);
    font-family: "Montserrat", sans-serif;
    position: relative;
  }
  .flyer {
    position: absolute;
    left: 21px; top: 121px;
    width: 740px; height: 958px;
    background: linear-gradient(135deg, #f7f7f7 0%, #ececec 55%, #f5f5f5 100%);
    box-shadow: 0 6px 18px rgba(0,0,0,.18);
    overflow: hidden;
  }
  .brand-name {
    position: absolute;
    top: 60px; left: 0; width: 100%;
    text-align: center;
    font-weight: 800;
    font-size: 62px;
    letter-spacing: 3px;
    color: var(--grey);
    line-height: 1;
  }
  .tagline {
    position: absolute;
    top: 143px; left: 0; width: 100%;
    text-align: center;
    font-weight: 700;
    font-size: 32px;
    color: var(--green);
    letter-spacing: -0.5px;
  }
  .tagline .sep { margin: 0 14px; font-weight: 600; }

  .doodle { position: absolute; border-radius: 50%; }
  .doodle-top { left: 351px; top: 213px; width: 57px; height: 62px; background: radial-gradient(#e2e2e2, transparent 70%); }
  .doodle-plate { left: 41px; top: 732px; width: 161px; height: 123px; background: radial-gradient(#e3ddd6, #ececec 60%, transparent 72%); }
  .doodle-bowl { left: 520px; top: 773px; width: 85px; height: 85px; background: radial-gradient(#e1e6d7, #ececec 65%, transparent 72%); }

  .card {
    position: absolute;
    width: 256px; height: 478px;
    background: #fff;
    border: 4px solid #fff;
    border-radius: 10px;
    box-shadow: 0 8px 16px rgba(0,0,0,.18);
    overflow: hidden;
    text-align: center;
    color: var(--ink);
  }
  .card-horizon { left: 29px; top: 222px; }
  .card-evergreen { left: 455px; top: 222px; }
  .card-amber { left: 243px; top: 289px; z-index: 2; }

  .card-head {
    position: absolute; left: 0; top: 0; width: 100%; height: 100px;
    border-radius: 6px 6px 50% 50% / 6px 6px 28px 28px;
    color: #fff; font-weight: 700; font-size: 23px; letter-spacing: 1px;
    padding-top: 28px;
  }
  .card-amber .card-head { padding-top: 34px; }
  .card-horizon .card-head, .card-horizon .price-band { background: var(--green); box-shadow: 0 6px 0 var(--green-dark); }
  .card-amber .card-head, .card-amber .price-band { background: var(--orange); box-shadow: 0 6px 0 var(--orange-dark); }
  .card-evergreen .card-head, .card-evergreen .price-band { background: var(--grey); box-shadow: 0 6px 0 var(--grey-dark); }
  .card-evergreen .card-head { padding-top: 42px; }
  .card .price-band { box-shadow: 0 -6px 0 rgba(0,0,0,.12); }

  .step {
    position: absolute; left: 50%; top: 128px; transform: translateX(-50%);
    width: 42px; height: 42px; border-radius: 50%;
    color: #fff; font-weight: 700; font-size: 28px; line-height: 42px;
    border: 3px solid #fff; box-shadow: 0 0 0 2px currentColor;
  }
  .card-horizon .step { background: var(--green); color: #fff; box-shadow: 0 0 0 2px var(--green); }
  .card-amber .step { background: var(--orange); box-shadow: 0 0 0 2px var(--orange); }
  .card-evergreen .step { background: var(--grey); box-shadow: 0 0 0 2px var(--grey); }
  .card-amber .step { top: 118px; }

  .package { position: absolute; left: 0; width: 100%; top: 172px; font-weight: 700; font-size: 25px; line-height: 25px; }
  .card-amber .package { top: 162px; }
  .days {
    position: absolute; left: 50%; transform: translateX(-50%); top: 228px;
    padding: 2px 20px; border-radius: 10px; color: #fff; font-size: 11px; font-weight: 700; letter-spacing: .5px;
  }
  .card-amber .days { top: 220px; }
  .card-horizon .days { background: var(--green); }
  .card-amber .days { background: var(--orange); }
  .card-evergreen .days { background: var(--grey); }

  .divider { position: absolute; left: 40px; right: 40px; top: 258px; height: 1px; background: var(--line); }
  .divider::after { content: ""; position: absolute; left: 50%; top: -1px; width: 32px; height: 3px; margin-left: -16px; background: var(--green); }
  .card-amber .divider { top: 250px; }

  .meals { position: absolute; left: 0; width: 100%; top: 284px; font-weight: 700; font-size: 20px; line-height: 25px; }
  .card-amber .meals { top: 278px; }

  .price-label {
    position: absolute; left: 50%; transform: translateX(-50%); top: 355px;
    width: 130px; height: 30px; border-radius: 8px; color: #fff;
    font-weight: 700; font-size: 23px; line-height: 30px; z-index: 2;
  }
  .card-amber .price-label { top: 352px; }
  .card-horizon .price-label { background: var(--ink); }
  .card-amber .price-label { background: var(--green); }
  .card-evergreen .price-label { background: var(--orange); }

  .price-band {
    position: absolute; left: 0; bottom: 0; width: 100%; height: 110px;
    border-radius: 50% 50% 6px 6px / 28px 28px 6px 6px;
    color: #fff; font-family: "Oswald", sans-serif; font-weight: 700; font-size: 44px;
    line-height: 1; padding-top: 32px; text-shadow: 0 2px 3px rgba(0,0,0,.25);
  }
  .card-amber .price-band { height: 112px; padding-top: 40px; }

  .save-tag {
    position: absolute; width: 100px; height: 52px; z-index: 3;
    background: var(--red); color: #fff; border-radius: 6px 4px 4px 6px;
    font-weight: 800; font-size: 15px; line-height: 16px; text-align: center;
    padding: 10px 0 0 16px; box-shadow: 0 3px 6px rgba(0,0,0,.25);
    outline: 1px dashed rgba(255,255,255,.6); outline-offset: -4px;
  }
  .save-tag::before { content: ""; position: absolute; left: 7px; top: 21px; width: 9px; height: 9px; border-radius: 50%; background: #fff; }
  .save-amber { left: 353px; top: 782px; transform: rotate(20deg); }
  .save-evergreen { left: 597px; top: 714px; transform: rotate(20deg); }

  .footer {
    position: absolute; left: 0; bottom: 0; width: 100%; height: 71px;
    background: var(--green);
    display: flex; align-items: center; justify-content: center;
    font-weight: 700; font-size: 21px; letter-spacing: 2.5px; color: var(--ink);
  }
  .footer-badge {
    position: absolute; left: 0; bottom: 0; width: 88px; height: 78px;
    background: #fff; border-radius: 0 40px 0 0;
  }
  .footer-badge::after { content: ""; position: absolute; left: 22px; top: 18px; width: 42px; height: 42px; border-radius: 50%; background: var(--grey); }
</style>
</head>
<body>
  <main class="flyer">
    <h1 class="brand-name">BRAMBLEFORK</h1>
    <p class="tagline">HEALTHY KITCHEN<span class="sep">|</span>MEAL PREP</p>

    <div class="doodle doodle-top" role="img" aria-label="Faint line drawing of a hot dog and leaf"></div>
    <div class="doodle doodle-plate" role="img" aria-label="Faint line drawing of a plated meal with vegetables"></div>
    <div class="doodle doodle-bowl" role="img" aria-label="Faint line drawing of a salad bowl"></div>

    <section class="card card-horizon">
      <div class="card-head">HORIZON</div>
      <div class="step">1</div>
      <div class="package">WEEK<br>PACKAGE</div>
      <div class="days">(7 DAYS )</div>
      <div class="divider"></div>
      <div class="meals">2 MEALS<br>A DAY</div>
      <div class="price-label">PRICE</div>
      <div class="price-band">$195.00</div>
    </section>

    <section class="card card-evergreen">
      <div class="card-head">EVERGREEN</div>
      <div class="step">6</div>
      <div class="package">WEEK<br>PACKAGE</div>
      <div class="days">(45 DAYS )</div>
      <div class="divider"></div>
      <div class="meals">2 MEALS<br>PER DAY</div>
      <div class="price-label">PRICE</div>
      <div class="price-band">$1080.00</div>
    </section>

    <section class="card card-amber">
      <div class="card-head">AMBER</div>
      <div class="step">3</div>
      <div class="package">WEEK<br>PACKAGE</div>
      <div class="days">(21 DAYS )</div>
      <div class="divider"></div>
      <div class="meals">2 MEALS<br>PER DAY</div>
      <div class="price-label">PRICE</div>
      <div class="price-band">$546.00</div>
    </section>

    <div class="save-tag save-amber">SAVE<br>$42.00!</div>
    <div class="save-tag save-evergreen">SAVE<br>$180!</div>

    <footer class="footer">www.brambleforkmeals.com</footer>
    <div class="footer-badge"></div>
  </main>
</body>
</html>
```